Charter Tour Boat Webpage Design

We need a web page design for a new business - Kelpwave Trips Orrinbah, We do Fishing Charters, Montague Island Eco Tours, Diving, Whale Watching. We currently have a very basic website up. www.kelpwavetripsorrinbah.com and as you can see we need a much better one.

Thanks!

Mainly fisherman, and families for tours

Business

• page for fishing, montague island eco tours, whale watching.
Contact page, and enquiry page with form.

```html
<!DOCTYPE html>
<html lang="en">
<head>
<meta charset="utf-8">
<title>Kelpwave Trips Orrinbah</title>
<link rel="stylesheet" href="https://fonts.googleapis.com/css2?family=Playfair+Display:ital,wght@0,700;1,400&family=Open+Sans:wght@400&display=swap">
<style>
  :root {
    --page-bg: #e3e1dc;
    --top-band: #d5d3ce;
    --accent: #1cc6da;
    --dark-panel: #241b17;
    --dark-panel-2: #2b221d;
    --card-bg: #fafafa;
    --title-ink: #4e4e4e;
    --body-ink: #3f3f3f;
    --muted-ink: #555555;
    --white: #ffffff;
  }
  * { margin: 0; padding: 0; box-sizing: border-box; }
  html, body { width: 1200px; height: 1113px; overflow: hidden; background: var(--page-bg); }
  .site {
    position: relative; width: 1024px; height: 950px;
    transform: scale(1.171875); transform-origin: 0 0;
    background: var(--page-bg);
    font-family: Arial, Helvetica, sans-serif;
  }
  .top-band { position: absolute; left: 0; top: 0; width: 1024px; height: 50px;
    background: var(--top-band); border-top: 1px solid var(--accent); }
  .social { position: absolute; top: 18px; right: 35px; display: flex; gap: 9px; }
  .social span { width: 21px; height: 21px; border-radius: 3px; background: #3f8fc8; display: block; }
  .social span:nth-child(2) { background: #3b5b9a; }
  .social span:nth-child(3) { background: #2a7fb0; }
  .brand { position: absolute; left: 61px; top: 84px; font-family: "Playfair Display", Georgia, serif;
    font-weight: 700; font-size: 29px; color: var(--title-ink); letter-spacing: -0.3px; }
  .main-nav { position: absolute; left: 33px; top: 158px; width: 960px; height: 52px;
    background: var(--dark-panel); border-radius: 4px; }
  .main-nav::before { content: ""; position: absolute; left: 66px; top: 0;
    border: 6px solid transparent; border-top-color: var(--accent); }
  .main-nav a { position: absolute; top: 17px; color: var(--accent); font-size: 16px;
    text-decoration: none; transform: translateX(-50%); white-space: nowrap; }
  .categories { position: absolute; left: 34px; top: 211px; width: 292px; height: 344px;
    background: var(--dark-panel-2); border-radius: 4px; }
  .categories h2 { position: absolute; left: 25px; top: 16px; font-family: "Playfair Display", Georgia, serif;
    font-style: italic; font-weight: 400; font-size: 24px; color: var(--white); }
  .categories .rule { position: absolute; left: 21px; top: 53px; width: 248px; border-top: 1px dashed #ddd; }
  .categories ul { list-style: none; position: absolute; left: 36px; top: 90px; width: 200px; }
  .categories li { height: 48px; padding-left: 7px; padding-top: 4px; color: var(--white); font-size: 14px;
    border-bottom: 1px dashed #bbb; word-spacing: 4px; }
  .categories li:nth-child(1), .categories li:nth-child(2) { border-bottom-color: var(--accent); }
  .categories li:last-child { border-bottom: none; padding-left: 11px; }
  .gallery { position: absolute; left: 327px; top: 211px; width: 666px; height: 343px;
    display: grid; grid-template-columns: 223px 228px 215px; grid-template-rows: 173px 170px; gap: 1px 0;
    border-radius: 4px; overflow: hidden; }
  .gallery div { display: block; }
  .ph-dive { background: linear-gradient(160deg, #1a7fa6, #0d3f63); }
  .ph-island { background: linear-gradient(180deg, #2a8fe0 0%, #1660b8 40%, #3aa36a 60%, #0e4fa0 100%); }
  .ph-angler { background: linear-gradient(180deg, #3e7fd8 0%, #1a4d9c 55%, #e9eef3 100%); }
  .ph-divers { background: linear-gradient(170deg, #4a86c8, #1c4f92); }
  .ph-orca { background: linear-gradient(180deg, #3a78b8 0%, #c9dff0 60%, #2c6aa6 100%); }
  .ph-shell { background: linear-gradient(180deg, #5f9be0 0%, #2b5d9c 45%, #6a4a36 70%, #3a2a20 100%); }
  .content { position: absolute; left: 33px; top: 560px; width: 960px; height: 323px;
    background: var(--card-bg); border-radius: 4px; }
  .welcome { position: absolute; left: 36px; top: 30px; width: 598px; }
  .welcome h1 { font-weight: 400; font-size: 20px; color: var(--accent); margin-left: 2px; margin-bottom: 14px; }
  .welcome p { font-family: "Open Sans", Verdana, sans-serif; font-size: 12.6px; line-height: 20px;
    color: var(--body-ink); text-align: justify; margin-bottom: 20px; }
  .divider { position: absolute; left: 674px; top: 30px; height: 236px; border-left: 1px dashed #aaa; }
  .contact-block { position: absolute; left: 705px; top: 30px; }
  .contact-block h2 { font-weight: 400; font-size: 21px; color: var(--accent); padding-left: 40px; position: relative; }
  .contact-block h2 svg { position: absolute; left: 0; top: -2px; }
  .contact-block address { font-style: normal; font-size: 14px; line-height: 17px; color: var(--muted-ink);
    margin: 27px 0 0 9px; }
  .contact-block address p { margin-bottom: 17px; }
  .footer-copy { position: absolute; left: 356px; top: 905px; font-size: 11px; color: #444; }
  .footer-links { position: absolute; left: 831px; top: 905px; font-size: 11px; color: #444; word-spacing: 1px; }
  .footer-links a { color: inherit; text-decoration: none; margin-right: 6px; }
</style>
</head>
<body>
<div class="site">
  <header class="top-band">
    <div class="social" aria-label="Social links"><span></span><span></span><span></span></div>
  </header>
  <div class="brand">Kelpwave Trips Orrinbah</div>

  <nav class="main-nav">
    <a href="#" style="left:74px">Home</a>
    <a href="#" style="left:201px">Fishing</a>
    <a href="#" style="left:361px">Montague Island</a>
    <a href="#" style="left:545px">Whale Watching</a>
    <a href="#" style="left:715px">Book Now</a>
    <a href="#" style="left:845px">Contact Us</a>
  </nav>

  <aside class="categories">
    <h2>Categories</h2>
    <div class="rule"></div>
    <ul>
      <li>Fishing</li>
      <li>Montague Island Eco Tours</li>
      <li>Diving</li>
      <li>Snorkeling</li>
      <li>Whale Watching</li>
    </ul>
  </aside>

  <section class="gallery">
    <div class="ph-dive" role="img" aria-label="Diver swimming underwater"></div>
    <div class="ph-island" role="img" aria-label="Island surrounded by blue sea"></div>
    <div class="ph-angler" role="img" aria-label="Angler reeling in a fish from a boat"></div>
    <div class="ph-divers" role="img" aria-label="Two scuba divers near a reef"></div>
    <div class="ph-orca" role="img" aria-label="Orca leaping from the water"></div>
    <div class="ph-shell" role="img" aria-label="Seashell on a beach"></div>
  </section>

  <main class="content">
    <div class="welcome">
      <h1>Welcome to Kelpwave Trips Orrinbah!</h1>
      <p>Rory Haldane has return from travelling and fishing Australia, to start Kelpwave Trips Orrinbah. Previous manager/operator of Saltline, Bluewater Sport Tours.We offer fully catered trips ranging from 2 to 9 hours weather fishing, diving, snorkeling, whale watching, Montague Island Eco Tour, or a mix of all our options.</p>
      <p>Specialising in small groups from shared charters to private with a personalised service.We use the latest top quality gear available from our fishing tackle, lures to electronics.Our boat is a 9.8 metre purpose built fishing and tour boat, with toilet and cooking facilities.We offer tea, coffee, soft drinks, water, light refreshments on all our charters/tours and lunch is provided on a full day fishing charter.</p>
    </div>
    <div class="divider"></div>
    <div class="contact-block">
      <h2>
        <svg width="30" height="30" viewBox="0 0 30 30" aria-hidden="true">
          <path d="M3 14 A12 12 0 0 1 27 10 Z" fill="#2bb3c9"/>
          <path d="M15 12 L11 28" stroke="#777" stroke-width="1.5"/>
          <ellipse cx="11" cy="28" rx="9" ry="2" fill="#e8d9a8"/>
        </svg>
        Contact us
      </h2>
      <address>
        <p>Kelpwave Trips Orrinbah<br>PO Box 704<br>ORRINBAH&nbsp; NSW&nbsp; 2593</p>
        <p>Email:<br>rory@kelpwavetripsorrinbah.com</p>
        <p>Phone: 0400 555 218</p>
      </address>
    </div>
  </main>

  <footer>
    <div class="footer-copy">Copyright © 2012 Kelpwave Trips Orrinbah Pty Ltd</div>
    <div class="footer-links"><a href="#">Terms &amp; Conditions</a><a href="#">Privacy</a></div>
  </footer>
</div>
</body>
</html>
```